Business card for Luxury Portable Restroom Trailer company

We are a Luxury Portable Restroom Trailer Company Called PELIKAR HIRES. Based in Orange County California. We provide portable restroom trailers for events, such as, Weddings, Concerts, Charity events, Sporting events, Tournaments, Corporate events, ect. We rent and Sell the Luxury restrooms. Our colors are white, grey, and Orange. As you will see in the logo we uploaded.
There are 2 people in the company so the names and titles will change for the 3 people but card will remain the same. Here is the information for each Person: Dennis Moyle CFO 555 018-3647
next Person: Wesley Tanford VP 555 018-3647
Next Person: Miles Tanford CEO 555 018-3647
Information to include on the card: Luxury Restroom Trailers Rental and Sales. Weddings, Concerts, Charity, Sporting and Corp. Events.

```html
<!DOCTYPE html>
<html lang="en">
<head>
<meta charset="UTF-8">
<title>PELIKAR HIRES – Business Card</title>
<link rel="stylesheet" href="https://fonts.googleapis.com/css2?family=Saira+Condensed:wght@600&family=Source+Sans+3:wght@400;700;800&display=swap">
<style>
  :root {
    --backdrop: #979897;
    --card-white: #ffffff;
    --card-grey: #58585a;
    --ring-grey: #525254;
    --orange: #f26b24;
    --text-grey: #58595b;
    --white: #ffffff;
  }
  * { margin: 0; padding: 0; box-sizing: border-box; }
  html, body {
    width: 1200px;
    height: 1200px;
    overflow: hidden;
    background: var(--backdrop);
    font-family: "Source Sans 3", sans-serif;
  }
  .card {
    position: absolute;
    left: 231px;
    width: 736px;
    height: 451px;
    overflow: hidden;
  }
  .card-front { top: 116px; background: var(--card-white); }
  .card-back { top: 631px; background: var(--card-grey); }

  .brand-front {
    position: absolute;
    left: 40px;
    top: 58px;
    font-weight: 800;
    font-size: 40px;
    letter-spacing: 1px;
    color: var(--orange);
    line-height: 1;
  }
  .holder-name {
    position: absolute;
    left: 40px;
    top: 238px;
    font-family: "Saira Condensed", sans-serif;
    font-weight: 600;
    font-size: 44px;
    line-height: 1;
    color: var(--orange);
    text-transform: uppercase;
  }
  .contact {
    position: absolute;
    left: 40px;
    top: 287px;
    font-size: 29px;
    line-height: 1;
    color: var(--text-grey);
  }
  .contact-label { color: var(--orange); }
  .divider {
    position: absolute;
    left: 40px;
    top: 330px;
    width: 652px;
    height: 2px;
    background: var(--orange);
  }
  .tagline {
    position: absolute;
    left: 40px;
    top: 346px;
    width: 660px;
    font-size: 22px;
    line-height: 29px;
    color: var(--text-grey);
    letter-spacing: -0.2px;
  }

  .back-ring {
    position: absolute;
    left: 0;
    top: 0;
  }
  .brand-back {
    position: absolute;
    left: 0;
    width: 100%;
    top: 190px;
    text-align: center;
    font-weight: 800;
    font-size: 62px;
    letter-spacing: 2px;
    line-height: 1;
    color: var(--white);
  }
</style>
</head>
<body>
  <section class="card card-front">
    <div class="brand-front">PELIKAR HIRES</div>
    <h1 class="holder-name">Dennis Moyle CFO</h1>
    <p class="contact"><span class="contact-label">CONTACT:</span> 555 018-3647</p>
    <div class="divider"></div>
    <p class="tagline">Luxury Restroom Trailers Rental and Sales. Weddings, Concerts, Charity, Sporting and Corp. Events.</p>
  </section>

  <section class="card card-back">
    <svg class="back-ring" width="736" height="451" viewBox="0 0 736 451" aria-hidden="true">
      <circle cx="369" cy="229" r="330" fill="none" stroke="var(--ring-grey)" stroke-width="34"/>
    </svg>
    <div class="brand-back">PELIKAR HIRES</div>
  </section>
</body>
</html>
```